Business card design needed

Our modern electrical contracting company requires business card design utilising our logo and incorporating our tag line "Service when you need it". We specialise in assisting our customers 24/7 offering a breakdown service.

Industry/Entity Type

Electrical

Contact Information for Business Card

Marcus Penhale, Electrical contractor,Tel: (08) 8456 3071, Fax: (08) 8679 4315, Mob 0438 562 740, Email: marcus.penhale@brightwirepower.com.au, Web: www.brightwirepower.com.au

Requirements
Must have
• we require a 2 sided card.
Front- Logo, tag line and contact information.
Rear- service when you need it! Call now for our 24/7 breakdown service

```html
<!DOCTYPE html>
<html lang="en">
<head>
<meta charset="utf-8">
<title>Service when you need it – rear of card</title>
<link rel="stylesheet" href="https://fonts.googleapis.com/css2?family=Tinos:wght@700&display=swap">
<style>
  :root {
    --paper: #ffffff;
    --brand-blue: #0a3cf0;
    --brand-blue-light: #8a9ff7;
    --ink: #000000;
    --on-blue: #ffffff;
  }
  html, body {
    margin: 0;
    padding: 0;
    width: 1200px;
    height: 657px;
    overflow: hidden;
    background: var(--paper);
  }
  .card-rear {
    position: relative;
    width: 1200px;
    height: 657px;
    background: var(--paper);
    font-family: "Tinos", "Times New Roman", serif;
    font-weight: 700;
  }
  .edge-rule {
    position: absolute;
    left: 1197px;
    top: 0;
    width: 2px;
    height: 386px;
    background: var(--brand-blue);
  }
  .call-band {
    position: absolute;
    left: 39px;
    top: 319px;
    width: 1143px;
    height: 87px;
    background: var(--brand-blue-light);
    display: flex;
    align-items: flex-end;
    justify-content: center;
    box-sizing: border-box;
    padding: 0 50px 14px 0;
  }
  .call-band__text {
    margin: 0;
    color: var(--ink);
    font-size: 45px;
    line-height: 1;
    white-space: nowrap;
  }
  .tagline-band {
    position: absolute;
    left: 20px;
    top: 242px;
    width: 1144px;
    height: 86px;
    background: var(--brand-blue);
    display: flex;
    align-items: center;
    justify-content: center;
    box-sizing: border-box;
    padding: 0 40px 4px 0;
  }
  .tagline-band__text {
    margin: 0;
    color: var(--on-blue);
    font-size: 56px;
    line-height: 1;
    white-space: nowrap;
  }
</style>
</head>
<body>
  <main class="card-rear">
    <div class="edge-rule"></div>
    <div class="call-band">
      <p class="call-band__text">Call now for our 24/7 breakdown service</p>
    </div>
    <div class="tagline-band">
      <h1 class="tagline-band__text">Service when you need it!</h1>
    </div>
  </main>
</body>
</html>
```